Business Card Design Project

Need a business card with logo that is attached.
Company name: Tolmen Brisk Solutions, LLC
My name: Lorna Tolmen
Title: President
Phone number: 703-555-0148
Email: ltolmen@tolmenbrisksolutions.example
web site: www.tolmenbrisksolutions.example

Industry/Entity Type

Business

```html
<!DOCTYPE html>
<html lang="en">
<head>
<meta charset="utf-8">
<title>Tolmen Brisk Solutions, LLC — Business Card</title>
<link rel="stylesheet" href="https://fonts.googleapis.com/css2?family=Tinos:wght@400;700&display=swap">
<style>
  :root {
    --page: #ffffff;
    --card-top: #9e9d99;
    --card-bottom: #343c3e;
    --company-ink: #3e4a49;
    --brand-blue: #2a5cc8;
    --mark-circle: #2f7fd8;
    --contact-ink: #8c8b88;
  }
  html, body {
    margin: 0;
    padding: 0;
    width: 1200px;
    height: 1000px;
    overflow: hidden;
    background: var(--page);
  }
  .canvas {
    position: relative;
    width: 1200px;
    height: 1000px;
    font-family: "Tinos", "Times New Roman", serif;
  }
  .card {
    position: absolute;
    left: 76px;
    top: 183px;
    width: 1051px;
    height: 633px;
  }
  .card-top {
    position: absolute;
    left: 0; top: 0;
    width: 100%;
    height: 389px;
    background: var(--card-top);
  }
  .card-bottom {
    position: absolute;
    left: 0; top: 389px;
    width: 100%;
    height: 244px;
    background: var(--card-bottom);
  }
  .company-line {
    position: absolute;
    right: 20px;
    top: 8px;
    margin: 0;
    font-size: 36px;
    font-weight: 700;
    color: var(--company-ink);
    white-space: nowrap;
  }
  .brand {
    position: absolute;
    left: 34px;
    top: 147px;
    display: flex;
    align-items: center;
    gap: 26px;
  }
  .brand-dot {
    width: 180px;
    height: 180px;
    border-radius: 50%;
    background: var(--mark-circle);
    flex: none;
  }
  .brand-name {
    margin: 0;
    width: 330px;
    font-size: 36px;
    line-height: 46px;
    font-weight: 700;
    color: var(--brand-blue);
  }
  .holder {
    position: absolute;
    left: 610px;
    top: 170px;
    width: 420px;
    text-align: center;
    color: var(--brand-blue);
    font-weight: 700;
  }
  .holder-name {
    margin: 0;
    font-size: 50px;
    line-height: 60px;
  }
  .holder-title {
    margin: 6px 0 0;
    font-size: 40px;
    line-height: 50px;
  }
  .contact {
    position: absolute;
    left: 37px;
    top: 452px;
    margin: 0;
    padding: 0;
    list-style: none;
    font-size: 34px;
    line-height: 56px;
    font-weight: 700;
    color: var(--contact-ink);
  }
</style>
</head>
<body>
<div class="canvas">
  <section class="card">
    <div class="card-top"></div>
    <div class="card-bottom"></div>

    <h1 class="company-line">Tolmen Brisk Solutions, LLC</h1>

    <div class="brand">
      <div class="brand-dot"></div>
      <p class="brand-name">Tolmen Brisk Solutions, LLC</p>
    </div>

    <div class="holder">
      <p class="holder-name">Lorna Tolmen</p>
      <p class="holder-title">President</p>
    </div>

    <ul class="contact">
      <li>Phone number: 703-555-0148</li>
      <li>Email: ltolmen@tolmenbrisksolutions.example</li>
      <li>www.tolmenbrisksolutions.example</li>
    </ul>
  </section>
</div>
</body>
</html>
```